Brightway Inc. Business Card Design

Brightway Inc. is in search of a great clean design for our business cards!

Looking to incorporate our full logo and watermark on side one (however, I am open to having the text and watermark separated within the design.)

On side two, I am looking to have contact information (Name, Position, Phone #, Email, Website (www.thebrightway.ca). Can have the logo and/or watermark as part of the design if applicable.

Please add tagline "Where Shine Counts" on either side 1 or 2. This tagline can be in a sans serif, serif or cursive font as long as it compliments overall design. Capitalization can be title or sentence case depending on how it fits within the design.

Get creative!! Looking for a clean, crisp, premium design! Looking for a glossy card finish with spot UV features when printed. Cards will also be printed with rounded corners. Standard dimensions (3.5 x 2).

Target Market(s)

B2B - primary clients are business owners or property management corporations. (residential jobs are few and far between)

Industry/Entity Type

Business

Contact Information for Business Card

- clean, crisp design
- double sided
- spot UV accents and glossy finish upon printing
- standard business card size (3.5 x 2) with rounded corners
- please see project description for requirements per side

Font styles to use
Sans Serif

Requirements
Must have
• - adequate bleeds with print ready files
• - cohesive design elements between side 1 & 2
• - spot UV elements (can be on both sides or just one, use your discretion)
• - colour pallet should match the logo file provided
• - incorporate tagline "where shine counts" (this tagline can be in a serif or sans serif font as long as it is complimentary to the overall design.
Nice to have
• - Premium elements with a clean design
Should not have
• - Please omit cartoon or whimsical like designs, think premium.
• - Colours should not stray from the pallet of the provided logo.

```html
<!DOCTYPE html>
<html lang="en">
<head>
<meta charset="utf-8">
<title>Brightway Inc. Business Card</title>
<link href="https://fonts.googleapis.com/css2?family=Roboto:wght@400;500;700;900&display=swap" rel="stylesheet">
<style>
  :root {
    --teal: #13b8bf;
    --navy: #1c2658;
    --white: #ffffff;
    --grey: #b9bcc4;
    --ink: #1a1a1a;
    --stage: #2b2b2b;
  }
  * { margin: 0; padding: 0; box-sizing: border-box; }
  html, body { width: 1200px; height: 900px; overflow: hidden; }
  body {
    background: var(--stage);
    font-family: 'Roboto', Arial, sans-serif;
    position: relative;
  }
  .card {
    position: absolute;
    left: 250px;
    width: 700px;
    height: 400px;
    border-radius: 26px;
    overflow: hidden;
  }
  .card-front { top: 35px; background: var(--teal); }
  .card-back { top: 465px; background: var(--white); }

  .lockup {
    position: absolute;
    display: flex;
    flex-direction: column;
    align-items: flex-end;
  }
  .brand {
    display: flex;
    align-items: center;
    gap: 14px;
  }
  .brand-mark { width: 52px; height: 52px; background: var(--navy); flex: none; }
  .brand-name {
    font-weight: 900;
    font-size: 54px;
    letter-spacing: 1px;
    line-height: 1;
    text-transform: uppercase;
    white-space: nowrap;
  }
  .tagline {
    margin-top: 8px;
    font-weight: 700;
    text-transform: uppercase;
    letter-spacing: 1px;
    white-space: nowrap;
  }

  .card-front .lockup { left: 0; right: 0; top: 140px; align-items: center; }
  .card-front .brand-name { color: var(--white); }
  .card-front .tagline { color: var(--white); font-size: 15px; }
  .card-front .website {
    position: absolute; left: 0; right: 0; bottom: 40px;
    text-align: center; color: var(--white); font-size: 17px;
  }

  .back-band {
    position: absolute; left: 0; right: 0; bottom: 0; height: 160px;
    background: var(--teal);
    border-top: 10px solid var(--navy);
  }
  .card-back .lockup { left: 50px; top: 120px; }
  .card-back .brand { gap: 10px; }
  .card-back .brand-mark { width: 38px; height: 38px; }
  .card-back .brand-name { color: var(--teal); font-size: 38px; }
  .card-back .tagline { color: var(--navy); font-size: 11px; margin-top: 6px; }

  .person { position: absolute; right: 50px; top: 40px; text-align: right; }
  .person-name { color: var(--teal); font-weight: 700; font-size: 24px; }
  .person-role { color: var(--ink); font-size: 13px; font-weight: 500; text-transform: uppercase; }

  .contacts {
    position: absolute; right: 40px; bottom: 14px;
    list-style: none; color: var(--white); font-size: 18px;
  }
  .contacts li {
    display: flex; justify-content: flex-end; align-items: center;
    gap: 10px; height: 32px;
  }
  .contacts svg { width: 18px; height: 18px; fill: none; stroke: var(--white); stroke-width: 2; }
</style>
</head>
<body>

<section class="card card-front">
  <div class="lockup">
    <div class="brand">
      <span class="brand-mark"></span>
      <span class="brand-name">Brightway Inc.</span>
    </div>
    <p class="tagline">Where Shine Counts</p>
  </div>
  <p class="website">www.thebrightway.ca</p>
</section>

<section class="card card-back">
  <div class="back-band"></div>

  <div class="lockup">
    <div class="brand">
      <span class="brand-mark"></span>
      <span class="brand-name">Brightway Inc.</span>
    </div>
    <p class="tagline">Where Shine Counts</p>
  </div>

  <div class="person">
    <p class="person-name">Daniel R Hale</p>
    <p class="person-role">Owner</p>
  </div>

  <ul class="contacts">
    <li>416-555-0182
      <svg viewBox="0 0 24 24"><path d="M5 3h4l2 5-3 2a12 12 0 0 0 6 6l2-3 5 2v4a2 2 0 0 1-2 2A18 18 0 0 1 3 5a2 2 0 0 1 2-2z"/></svg>
    </li>
    <li>647.555.0139
      <svg viewBox="0 0 24 24"><rect x="6" y="2" width="12" height="20" rx="2"/><line x1="11" y1="18" x2="13" y2="18"/></svg>
    </li>
    <li>hello@thebrightway.ca
      <svg viewBox="0 0 24 24"><rect x="3" y="5" width="18" height="14"/><path d="M3 5l9 8 9-8"/></svg>
    </li>
    <li>www.thebrightway.ca
      <svg viewBox="0 0 24 24"><circle cx="12" cy="12" r="9"/><path d="M3 12h18M12 3c3 3 3 15 0 18M12 3c-3 3-3 15 0 18"/></svg>
    </li>
  </ul>
</section>

</body>
</html>
```